Massage Therapy and Personal Training Business Card (Lorvex Wellness)

I need a logo design based in Washington. The company is called Lorvex Wellness. Lorvex are my initials. I specialize in massage therapy and personal training and general wellness of my clients. I've tried getting designs but haven't quite yet found what I'm looking for. I'm not inclined to a certain color yet but some color that resembles wellness such as light blue and white or green and white. Again, I'm not really picky about that. Thank you in advance

Industry/Entity Type

Business

Contact Information for Business Card

Have the description on one side and space for writing information on the back side such as number, appt, etc. I have an example attached. I see a lot of these card. I dont want the exact one, but something similar. Simple, professional and elegant.

Colors

Designer to choose colors to be used in the design.

Requirements
Must have
• Space on the back side to write
• A professional, elegant look
Should not have
• cartoon like style.

```html
<!DOCTYPE html>
<html lang="en">
<head>
<meta charset="utf-8">
<title>Lorvex Wellness – Business Card</title>
<link rel="stylesheet" href="https://fonts.googleapis.com/css2?family=Cinzel:wght@400&family=Open+Sans:wght@400;600;700&display=swap">
<style>
  :root {
    --page-bg: #eeeeea;
    --green-light: #d6e573;
    --green-mid: #a8c950;
    --green-deep: #7aa83a;
    --ink: #1b1b1b;
    --band: #141414;
    --figure-light: #9fc25a;
    --figure-dark: #6f9a3a;
  }
  * { margin: 0; padding: 0; box-sizing: border-box; }
  html, body { width: 1200px; height: 1000px; overflow: hidden; }
  body {
    background: var(--page-bg);
    font-family: "Open Sans", Arial, sans-serif;
    color: var(--ink);
    position: relative;
  }
  .card {
    position: absolute;
    left: 266px;
    width: 666px;
    height: 396px;
    border-radius: 24px;
    overflow: hidden;
    background: radial-gradient(ellipse 60% 65% at 55% 50%, var(--green-light) 0%, var(--green-mid) 60%, var(--green-deep) 100%);
    box-shadow: 0 6px 14px rgba(0,0,0,0.25);
  }
  .card--front { top: 74px; }
  .card--back { top: 534px; }

  .anatomy-art {
    position: absolute;
    left: 30px; top: 0;
    width: 310px; height: 370px;
    background: linear-gradient(180deg, var(--figure-light) 0%, var(--figure-dark) 100%);
    border-radius: 40% 40% 8% 8% / 20% 20% 4% 4%;
    opacity: 0.85;
  }
  .base-band { position: absolute; left: 0; bottom: 0; width: 666px; height: 60px; }

  .front-info {
    position: absolute;
    left: 330px; width: 326px;
    top: 148px;
    text-align: center;
  }
  .brand-name {
    font-family: "Cinzel", "Times New Roman", serif;
    font-size: 31px;
    line-height: 1;
    letter-spacing: 0.5px;
    white-space: nowrap;
  }
  .brand-tagline { font-size: 19px; margin-top: 8px; }
  .therapist-name { font-size: 19px; margin-top: 26px; }
  .therapist-role { font-size: 16px; margin-top: 2px; }
  .contact { font-size: 16px; margin-top: 10px; line-height: 22px; }

  .back-title {
    position: absolute; top: 28px; width: 100%;
    text-align: center; font-weight: 600; font-size: 19px;
  }
  .write-line {
    position: absolute; left: 136px; width: 394px;
    border-top: 2px solid var(--ink);
  }
  .write-line--name { top: 131px; }
  .write-line--when { top: 262px; }
  .field-label { position: absolute; font-weight: 600; font-size: 16px; }
  .label-name { top: 140px; left: 0; width: 666px; text-align: center; }
  .label-date { top: 271px; left: 222px; }
  .label-time { top: 271px; left: 406px; }

  .days {
    position: absolute; top: 188px; left: 32px; right: 32px;
    display: flex; justify-content: space-between;
  }
  .day { display: flex; align-items: center; gap: 12px; font-weight: 600; font-size: 16px; }
  .day-box {
    width: 26px; height: 18px;
    border: 2px solid var(--ink); border-radius: 6px;
  }
  .policy {
    position: absolute; top: 324px; width: 100%; text-align: center;
  }
  .policy-title { font-weight: 600; font-size: 16px; }
  .policy-text { font-size: 16px; margin-top: 2px; }
</style>
</head>
<body>

<section class="card card--front">
  <div class="anatomy-art" role="img" aria-label="Anatomical illustration of a human back and shoulder muscles with highlighted pressure points"></div>
  <svg class="base-band" viewBox="0 0 666 60" aria-hidden="true">
    <path d="M0 10 Q333 55 666 0 L666 60 L0 60 Z" fill="var(--band)"/>
  </svg>
  <div class="front-info">
    <div class="brand-name">LORVEX WELLNESS</div>
    <div class="brand-tagline">Message Therapy</div>
    <div class="therapist-name">DANIEL MERCER</div>
    <div class="therapist-role">Massage Therapist</div>
    <div class="contact">0455218306<br>info@lorvexwellness.com</div>
  </div>
</section>

<section class="card card--back">
  <div class="back-title">YOUR&nbsp; NEXT APPOINTMENT</div>
  <div class="write-line write-line--name"></div>
  <div class="field-label label-name">NAME</div>
  <div class="days">
    <div class="day">Mon <span class="day-box"></span></div>
    <div class="day">Tue <span class="day-box"></span></div>
    <div class="day">Wed <span class="day-box"></span></div>
    <div class="day">Thur <span class="day-box"></span></div>
    <div class="day">Fri <span class="day-box"></span></div>
    <div class="day">Sat <span class="day-box"></span></div>
  </div>
  <div class="write-line write-line--when"></div>
  <div class="field-label label-date">DATE</div>
  <div class="field-label label-time">TIME</div>
  <div class="policy">
    <div class="policy-title">CANCELATION POLICY</div>
    <div class="policy-text">If you are unable to keep your appointment , please allow 24 hours notice</div>
  </div>
</section>

</body>
</html>
```